Business Card needed for International Migration and Education business

we are based in Australia, the business is called 'FarReach Relocation' and its sister business for international education is called 'FarReach Learning' - we need the design for the business 'FarReach Relocation' - FarReach Relocation is about migration to Australia (but not limited to Australia only therefore purely Australian look would not fit). We would like to see designs that use the color blue or acqua and maybe orange..all those colours don't have to be used together and not only those colours are to be used. We are looking for a modern design. The final design should communicate modern thinking, professionalism, dynamism, confidence. We would like to use the same business card design for our sister business "FarReach Learning" - which is business about studying in different countries as we recruit students to study in Australia, USA, New Zealand, Canada, UK etc. We would like to be able the final design to be easily changed by us to fit the 'FarReach Learning' business - we would only change the contact text (email address etc)

The information to be included in the business card: Tessa Virnaud Managing Director Migration Agent MARN 0917264 FarReach Relocation postal address: PO Box 2749, Carlwood East VIC 3179, Australia mobile: 0417296031 office address: Level 1, 287 Fenwick Road, Ardmere VIC 3211 web www.farreachrelocation-example.com telephone: 61 3 8714 6023 fax + 61 3 8735 2910 email: tessa@farreachrelocation-example.com

```html
<!DOCTYPE html>
<html lang="en">
<head>
<meta charset="utf-8">
<title>FarReach Relocation – Business Card</title>
<link rel="stylesheet" href="https://fonts.googleapis.com/css2?family=Open+Sans:wght@400;600&display=swap">
<style>
  :root {
    --stage: #e4e4e4;
    --card-top: #ffffff;
    --card-bottom: #e9e9ea;
    --ink: #1c1c1c;
    --accent: #1aa3d9;
    --icon-bg: #1aa3d9;
  }
  * { box-sizing: border-box; margin: 0; padding: 0; }
  html, body {
    width: 1200px; height: 948px; overflow: hidden;
    background: var(--stage);
    font-family: "Open Sans", Arial, sans-serif;
    color: var(--ink);
  }
  .card {
    position: absolute; left: 100px; top: 188px;
    width: 1000px; height: 572px;
    background: linear-gradient(160deg, var(--card-top) 0%, var(--card-bottom) 100%);
    box-shadow: 0 14px 34px rgba(0,0,0,0.22);
    overflow: hidden;
  }
  .side-band {
    position: absolute; right: 0; top: 0;
    width: 26px; height: 400px;
    background: var(--accent);
  }
  .corner-arc {
    position: absolute; left: -44px; bottom: -44px;
    width: 88px; height: 88px; border-radius: 50%;
    background: var(--accent);
  }
  .brand {
    position: absolute; left: 62px; top: 150px;
    display: flex; align-items: center; gap: 12px;
  }
  .brand-dot {
    width: 52px; height: 52px; border-radius: 50%;
    background: var(--accent);
  }
  .brand-name {
    font-size: 34px; font-weight: 600; color: var(--ink);
    letter-spacing: 0.5px;
  }
  .person {
    position: absolute; left: 72px; top: 440px;
  }
  .person-name {
    font-size: 34px; font-weight: 600; color: var(--accent); line-height: 1.2;
  }
  .person-role {
    font-size: 31px; font-weight: 400; color: var(--ink); line-height: 1.2;
  }
  .contact {
    position: absolute; right: 82px; top: 52px;
    text-align: right;
    font-size: 20px; line-height: 30px;
  }
  .contact p { position: relative; white-space: nowrap; }
  .contact .gap { margin-top: 30px; }
  .contact .web span { color: var(--accent); }
  .icon {
    position: absolute; right: -40px; top: 4px;
    width: 22px; height: 22px;
  }
</style>
</head>
<body>
  <main class="card">
    <div class="side-band"></div>
    <div class="corner-arc"></div>

    <div class="brand">
      <div class="brand-dot"></div>
      <span class="brand-name">FarReach Relocation</span>
    </div>

    <div class="person">
      <p class="person-name">Tessa Virnaud</p>
      <p class="person-role">Managing Director</p>
    </div>

    <section class="contact">
      <p>Mobile: 0417296031</p>
      <p>Migration Agent MARN 0917264</p>
      <p>FarReach Relocation Postal Address: PO Box</p>
      <p>2749, Carlwood East VIC 3179, Australia</p>
      <p class="gap">Office Address: Level 1, 287</p>
      <p>Fenwick Road, Ardmere VIC 3211
        <svg class="icon" viewBox="0 0 22 22" aria-hidden="true"><circle cx="11" cy="11" r="11" fill="var(--icon-bg)"/><path d="M11 5a4 4 0 0 0-4 4c0 3 4 8 4 8s4-5 4-8a4 4 0 0 0-4-4zm0 5.5a1.5 1.5 0 1 1 0-3 1.5 1.5 0 0 1 0 3z" fill="#fff"/></svg>
      </p>
      <p>+ 61 3 8735 2910
        <svg class="icon" viewBox="0 0 22 22" aria-hidden="true"><circle cx="11" cy="11" r="11" fill="var(--icon-bg)"/><rect x="6" y="8" width="10" height="7" rx="1" fill="#fff"/><rect x="8" y="5" width="6" height="4" fill="#fff"/></svg>
      </p>
      <p>61 3 8714 6023
        <svg class="icon" viewBox="0 0 22 22" aria-hidden="true"><circle cx="11" cy="11" r="11" fill="var(--icon-bg)"/><path d="M8 6l2 2.5-1.2 1.4a7 7 0 0 0 3.3 3.3L13.5 12 16 14l-1.2 1.8C11 16 6 11 6.2 7.2z" fill="#fff"/></svg>
      </p>
      <p class="web">www.<span>farreachrelocation-example</span>.com
        <svg class="icon" viewBox="0 0 22 22" aria-hidden="true"><circle cx="11" cy="11" r="11" fill="var(--icon-bg)"/><rect x="5.5" y="7" width="11" height="8" rx="1" fill="#fff"/><path d="M5.5 7.5l5.5 4 5.5-4" stroke="var(--icon-bg)" stroke-width="1.2" fill="none"/></svg>
      </p>
      <p>tessa@farreachrelocation-example.com</p>
    </section>
  </main>
</body>
</html>
```